Financial services firm needs updated web design

Our current website, coinpathwealth.example was created by ourselves using templates provided by our website host, Harborline Webworks. We are looking to get a whole new look and feel to our website that is clean, professional and easy to navigate. The design must be able to be transferred to Harborline Webworks for hosting (FTP??-outside my area of expertise - sorry) and that the information can be updated and changed by ourselves in the future. I have included our updated logo and our business card design.
Updates
Project Deadline Extended
Reason: Went away on vacation for two weeks.
Target Market(s)
Age 50+ individuals looking for investment, retirement and estate planning guidance.
Industry/Entity Type
Financial
Number of Pages Required
1 page
Font styles to use
Other font styles liked:
- Adobe Caslon Pro
Look and feel
Each slider illustrates characteristics of the customer's brand and the style your logo design should communicate.

```html
<!DOCTYPE html>
<html lang="en">
<head>
<meta charset="utf-8">
<title>coinpathwealth</title>
<link rel="stylesheet" href="https://fonts.googleapis.com/css2?family=Open+Sans:wght@400&family=Questrial&family=Arimo:wght@400;700&display=swap">
<style>
:root{
  --green:#4f9a3e;
  --green-dark:#3a7f2c;
  --green-light:#7fc06a;
  --ink:#222;
  --body:#444;
  --line:#e4e4e4;
  --footer-head:#a9a9a9;
}
*{margin:0;padding:0;box-sizing:border-box}
html,body{width:1200px;height:1200px;overflow:hidden;background:#fff}
body{position:relative;font-family:'Arimo',Arial,sans-serif;color:var(--ink)}
.abs{position:absolute}

/* header */
.site-header{left:0;top:0;width:1200px;height:94px;background:#fff;border-bottom:1px solid #ddd}
.brand{left:171px;top:28px;display:flex;align-items:center;gap:10px}
.brand-mark{width:14px;height:14px;background:var(--green)}
.brand-name{font-family:'Arimo',Arial,sans-serif;font-size:30px;font-weight:400;color:var(--green);line-height:1}
.phone{right:176px;top:12px;font-size:17px;display:flex;align-items:center;gap:4px;color:#111}
.main-nav a{position:absolute;top:52px;height:42px;line-height:42px;font-size:12.5px;color:#222;text-decoration:none}
.main-nav a.active{background:linear-gradient(#5fae4a,var(--green-dark));color:#fff;padding:0 17px;border-radius:3px 3px 0 0}

/* hero */
.hero{left:0;top:95px;width:1200px;height:304px;background:
 radial-gradient(ellipse 45% 60% at 50% 45%,#6b6f78 0%,#9a9ca3 45%,transparent 75%),
 linear-gradient(90deg,#e8e8e8 0%,#bcbcbe 20%,#8d8f95 50%,#bcbcbe 80%,#e8e8e8 100%)}
.hero-caption{left:146px;top:220px;width:908px;height:84px;background:linear-gradient(90deg,rgba(40,40,40,0),rgba(40,40,40,.85) 15%,rgba(40,40,40,.85) 85%,rgba(40,40,40,0))}
.hero-caption p{position:absolute;left:0;right:0;top:24px;text-align:center;color:#fff;font-size:26px}
.dots{left:572px;display:flex;gap:8px}
.dots span{width:7px;height:7px;background:#fff}
.dots span.on{background:var(--green-light)}

/* featured */
.section-title{left:179px;top:428px;font-size:19px;color:#223;font-weight:400}
.title-rule{left:349px;top:433px;width:628px;height:15px;background:repeating-linear-gradient(135deg,#ddd 0 1px,#fff 1px 3px)}
.carousel-arrows{left:981px;top:432px;display:flex;gap:3px}
.carousel-arrows span{width:19px;height:16px;border:1px solid #ccc;background:#f2f2f2;display:flex;align-items:center;justify-content:center}
.service-card{top:471px;width:197px;height:120px;border:1px solid #ccc}
.service-photo{height:96px}
.service-label{height:24px;line-height:24px;text-align:center;color:#fff;font-weight:700;font-size:13px;background:linear-gradient(#7cc067,var(--green-dark));text-shadow:0 1px 1px rgba(0,0,0,.4)}

/* welcome */
.welcome-title{left:180px;top:622px;font-family:'Questrial',sans-serif;font-size:20px;color:var(--green);font-weight:400}
.welcome-text{left:180px;top:654px;width:580px;font-family:'Open Sans',sans-serif;font-size:11px;line-height:20.5px;color:var(--body)}
.welcome-text p+p{margin-top:20.5px}
.video{left:769px;top:636px;width:257px;height:150px;background:linear-gradient(120deg,#5d6b5a 0%,#8a8c84 40%,#2c3440 100%)}
.video-tools{right:4px;top:6px;display:flex;flex-direction:column;gap:3px}
.video-tools span{width:19px;height:15px;background:#2b2b2b;border:1px solid #777}
.video-bar{left:0;bottom:0;width:257px;height:22px;background:rgba(0,0,0,.7)}
.play{left:5px;top:3px;width:32px;height:16px;background:#333;border:1px solid #666}
.progress{left:48px;top:9px;width:160px;height:4px;background:#555}
.progress i{display:block;width:70px;height:4px;background:#2a8fd8}

/* partners */
.partners{left:171px;top:827px;width:858px;height:65px;border:1px solid var(--line);display:flex}
.partner{flex:1;border-right:1px solid var(--line);display:flex;align-items:center;justify-content:center;font-size:17px;color:#8a8a8a;background:#fafafa}
.partner:last-child{border-right:0}
.partner.current{background:#fff}

/* footer */
.site-footer{left:0;top:930px;width:1200px;height:270px;background:linear-gradient(#1e1e1e,#0c0c0c 60%,#1a1a1a)}
.foot-col{top:965px;font-size:10.5px;line-height:16.3px;color:#fff}
.foot-col h4{font-size:11px;color:var(--footer-head);font-weight:700}
.foot-links{left:175px;font-size:10.5px;color:#9a9a9a}
.foot-links span{margin:0 4px;color:#666}
.copy{left:175px;top:1160px;font-size:10.5px;color:#8a8a8a}
.social{left:945px;top:1108px;display:flex;gap:5px}
.social span{width:23px;height:23px;border-radius:3px}
.payments{left:712px;top:1156px;display:flex;gap:14px;align-items:center;font-weight:700;color:#4a4a4a;font-size:14px}
.pay-badge{width:42px;height:24px;background:#555}
.ssl-badge{width:80px;height:26px;background:#3a3a3a;border-radius:3px}
</style>
</head>
<body>

<header class="site-header abs">
  <div class="brand abs"><span class="brand-mark"></span><span class="brand-name">coinpathwealth</span></div>
  <div class="phone abs">
    <svg width="14" height="18" viewBox="0 0 14 18"><path d="M4 1 L7 5 L5 7 Q6 11 9 13 L11 11 L13 14 L10 17 Q2 13 1 4 Z" fill="none" stroke="#111" stroke-width="1.5"/></svg>
    +1 555 010 2040
  </div>
  <nav class="main-nav">
    <a class="active" style="left:563px">Home</a>
    <a style="left:645px">About Us</a>
    <a style="left:727px">Services</a>
    <a style="left:804px">News</a>
    <a style="left:860px">Testimonials</a>
    <a style="left:955px">Contact Us</a>
  </nav>
</header>

<section class="hero abs" role="img" aria-label="Blurred photo of a business team standing together">
  <div class="hero-caption abs"><p>Morbi ornare ante quis nulla dictum imperdiet.</p></div>
  <div class="dots abs" style="top:287px"><span class="on"></span><span></span><span></span><span></span></div>
</section>

<h2 class="section-title abs">Featured Services</h2>
<div class="title-rule abs"></div>
<div class="carousel-arrows abs">
  <span><svg width="8" height="10"><path d="M6 1 L2 5 L6 9" fill="none" stroke="#555" stroke-width="1.5"/></svg></span>
  <span><svg width="8" height="10"><path d="M2 1 L6 5 L2 9" fill="none" stroke="#555" stroke-width="1.5"/></svg></span>
</div>

<div class="service-card abs" style="left:180px">
  <div class="service-photo" role="img" aria-label="Photo of hands using a calculator over financial papers" style="background:linear-gradient(135deg,#c9a58a,#e6e8ec 50%,#9aa3ad)"></div>
  <div class="service-label">Financial Planning</div>
</div>
<div class="service-card abs" style="left:394px">
  <div class="service-photo" role="img" aria-label="Photo of business people offering a handshake" style="background:linear-gradient(135deg,#3a4050,#8a8f98 50%,#23262e)"></div>
  <div class="service-label">Business Services</div>
</div>
<div class="service-card abs" style="left:608px">
  <div class="service-photo" role="img" aria-label="Photo of hands protecting a pink piggy bank" style="background:linear-gradient(135deg,#d9b8a5,#eaa9ba 50%,#f0e6e2)"></div>
  <div class="service-label">Financial Security</div>
</div>
<div class="service-card abs" style="left:822px">
  <div class="service-photo" role="img" aria-label="Photo of a couple meeting with an advisor" style="background:linear-gradient(135deg,#6b5a52,#b8b4b0 50%,#2e3038)"></div>
  <div class="service-label">Investment Planning</div>
</div>

<h2 class="welcome-title abs">Welcome to Company Name</h2>
<div class="welcome-text abs">
  <p>Morbi semper mattis malesuada. Donec ullamcorper rhoncus nisl. Cras laoreet sed turpis a ultrices. Vivamus ac elit dapibus, interdum mi ac, condimentum quam. Sed pharetra mi non nisl lacinia, at dictum nulla aliquam. Nam eget nisi a tellus accumsan ornare vel vitae leo.</p>
  <p>Nam convallis gravida condimentum. Morbi malesuada dui urna, vel elementum massa auctor adipiscing. Pellentesque habitant morbi tristique senectus et netus et malesuada fames ac turpis egestas.</p>
</div>

<div class="video abs" role="img" aria-label="Video still of a smiling senior advisor in an office">
  <div class="video-tools abs"><span></span><span></span><span></span></div>
  <div class="video-bar abs">
    <div class="play abs"><svg width="32" height="16"><path d="M13 4 L20 8 L13 12 Z" fill="#fff"/></svg></div>
    <div class="progress abs"><i></i></div>
  </div>
</div>

<div class="partners abs">
  <div class="partner">Ridgebank</div>
  <div class="partner current">Northmere Trust</div>
  <div class="partner">Veltro Motors</div>
  <div class="partner">Quadrion</div>
  <div class="partner">Fizzwell</div>
  <div class="partner">Autoguard</div>
</div>

<footer class="site-footer abs" role="img" aria-label="Dark night city skyline background"></footer>

<div class="foot-col abs" style="left:178px"><h4>New to Trading</h4>The Basics<br>Forex / CFDs<br>Futures<br>Options<br>NDFs</div>
<div class="foot-col abs" style="left:297px"><h4>Products</h4>ECN Forex Trading<br>CFD Trading<br>Futures<br>Options<br>NDFs</div>
<div class="foot-col abs" style="left:421px"><h4>Services</h4>Mobile Trading<br>AutoTrading<br>Fund Management</div>
<div class="foot-col abs" style="left:560px"><h4>Support</h4>Contact Us<br>Live Chat<br>Help Wiki<br>Trading Tips<br>Research</div>
<div class="foot-col abs" style="left:669px"><h4>Your Account</h4>Free Demo<br>Go Live<br>Fund your Account</div>
<div class="foot-col abs" style="left:787px"><h4>Become a Partner</h4>Why Financial<br>Introducing Brokers<br>Affiliates</div>
<div class="foot-col abs" style="left:912px"><h4>Money Managers</h4>Become a<br>Money Manager</div>

<div class="foot-links abs" style="top:1112px">Home<span>|</span>About Us<span>|</span>Services<span>|</span>News<span>|</span>Testimonials<span>|</span>Contact Us</div>
<div class="foot-links abs" style="top:1144px">Terms &amp; Conditions<span>|</span>Privacy Policy<span>|</span>Sitemap</div>
<div class="copy abs">© 2014 Company Name. All rights reserved.</div>

<div class="social abs">
  <span style="background:#3a9a3a" aria-label="Share"><svg width="23" height="23"><circle cx="7" cy="12" r="2.5" fill="#fff"/><circle cx="16" cy="7" r="2.5" fill="#fff"/><circle cx="16" cy="17" r="2.5" fill="#fff"/><path d="M7 12 L16 7 M7 12 L16 17" stroke="#fff" stroke-width="1.5"/></svg></span>
  <span style="background:#3b5da8" aria-label="Social network"></span>
  <span style="background:#3aa0dd" aria-label="Social network"></span>
</div>

<div class="payments abs">
  <span>CardOne</span>
  <span>PayCircle</span>
  <span>Walletly</span>
  <span class="pay-badge" aria-label="Bank transfer"></span>
  <span class="ssl-badge" aria-label="Security certificate"></span>
</div>

</body>
</html>
```